Plakate für Charity Unternehmen
Zielgruppe
Orno ist ein weltweit agierendes Charity Unternehmen.
Aufgabenstellung
Wir benötigen ein 'Plakat' Design, mit dem Zweck dieses Design als Banner, Sticker oder als Schild an unseren Projekten anzubringen. Das Schild soll in zwei verschiedenen Layouts geliefert werden.
1. Eine Art Blanko Version in der das Logo und das Motto eingearbeitet sind. Dieser Teil nimmt rund 1/3 des Plakats ein. Der Rest hat einen Freiraum auf dem wir Namen der Spender oder kooperative Charity Logos einsetzen können. Diese Version wird für Zusammenarbeit verwendet.
2. Eine zweite Version nimmt das gesamte Plakat ein, hier findet sich das Logo und das Motto welche das ganze Plakat einnehmen.
In beiden Fällen sollte die Aufteilung sauber und gut leserlich sein. Das Plakat wird in Auflösungen von bis zu 1,5m mal 1m gedruckt, sollte dementsprechend also die richtige Auflösung haben. Außerdem sollten Photoshop Datei möglichst mitgeliefert werden damit wir wenn nötig Namen und Logos einsetzen können.
Das einzuarbeitende Motto lautet:
إنما المؤمنون أخوة
Das Plakat sollte im Querformat sein und die Hintergrundfarbe sollte schwarz oder weiß sein.
Anbei befindet sich eine Beispieldatei wie das Plakat an den Projekten angebracht wird.

```html
<!DOCTYPE html>
<html lang="de">
<head>
<meta charset="utf-8">
<title>Orno – Plakate</title>
<link rel="stylesheet" href="https://fonts.googleapis.com/css2?family=Noto+Sans+Arabic:wght@700&family=Tinos&display=swap">
<style>
  :root {
    --page-bg: #e3e3e3;
    --poster-bg: #222222;
    --gold: #d1ac60;
    --gold-dark: #b69356;
    --helmet-gold: #cfae62;
    --blue-light: #2e7fc3;
    --blue-dark: #0c5a8a;
    --red-light: #cc4a28;
    --red-dark: #a31f22;
    --white: #ffffff;
  }
  * { margin: 0; padding: 0; box-sizing: border-box; }
  html, body { width: 1000px; height: 1200px; overflow: hidden; background: var(--page-bg); }
  .sheet { position: relative; width: 1000px; height: 1200px; }
  .poster {
    position: absolute; left: 107px; width: 786px; height: 523px;
    background: var(--poster-bg); overflow: hidden;
  }
  .poster--collab { top: 65px; }
  .poster--full { top: 612px; }
  .corner { position: absolute; top: 0; width: 178px; height: 230px; }
  .corner--left { left: 0; }
  .corner--right { right: 0; }
  .emblem {
    position: absolute; left: 50%; transform: translateX(-50%);
    background: linear-gradient(160deg, var(--helmet-gold), #c19f55);
    border-radius: 48% 48% 20% 30%;
  }
  .poster--collab .emblem { top: 43px; width: 122px; height: 184px; }
  .poster--full .emblem { top: 23px; width: 83px; height: 127px; }
  .brand-name {
    position: absolute; left: 0; right: 0; text-align: center;
    font-family: "Tinos", "Times New Roman", serif; font-weight: 400;
    color: var(--white); letter-spacing: 1px; line-height: 1;
  }
  .poster--collab .brand-name { top: 240px; font-size: 76px; }
  .poster--full .brand-name { top: 158px; font-size: 52px; }
  .motto-band {
    position: absolute; left: 0; width: 100%; height: 104px;
    background: linear-gradient(to bottom, var(--gold) 0%, var(--gold) 40%, var(--gold-dark) 100%);
    display: flex; align-items: center; justify-content: center;
  }
  .poster--collab .motto-band { top: 344px; }
  .poster--full .motto-band { top: 236px; }
  .motto {
    font-family: "Noto Sans Arabic", "Arial", sans-serif; font-weight: 700;
    font-size: 60px; color: var(--white); line-height: 1; direction: rtl;
    transform: translateY(-4px);
  }
</style>
</head>
<body>
<div class="sheet">

  <section class="poster poster--collab">
    <svg class="corner corner--left" viewBox="0 0 178 230" role="img" aria-label="Blaue polygonale Eckdekoration">
      <defs>
        <linearGradient id="blueFacetA" x1="0" y1="0" x2="1" y2="1">
          <stop offset="0" stop-color="var(--blue-dark)"/>
          <stop offset="0.5" stop-color="var(--blue-light)"/>
          <stop offset="1" stop-color="#2a7cbf"/>
        </linearGradient>
      </defs>
      <polygon points="0,0 178,0 157,18 138,104 114,111 17,194 0,230" fill="url(#blueFacetA)"/>
    </svg>
    <svg class="corner corner--right" viewBox="0 0 178 230" role="img" aria-label="Rote polygonale Eckdekoration">
      <defs>
        <linearGradient id="redFacetA" x1="1" y1="0" x2="0" y2="1">
          <stop offset="0" stop-color="var(--red-dark)"/>
          <stop offset="0.5" stop-color="var(--red-light)"/>
          <stop offset="1" stop-color="#c02e26"/>
        </linearGradient>
      </defs>
      <polygon points="178,0 0,0 21,18 40,104 64,111 161,194 178,230" fill="url(#redFacetA)"/>
    </svg>
    <div class="emblem" role="img" aria-label="Platz für das Bildzeichen von Orno"></div>
    <p class="brand-name">Orno</p>
    <div class="motto-band"><p class="motto" lang="ar">إنما المؤمنون أخوة</p></div>
  </section>

  <section class="poster poster--full">
    <svg class="corner corner--left" viewBox="0 0 178 230" role="img" aria-label="Blaue polygonale Eckdekoration">
      <defs>
        <linearGradient id="blueFacetB" x1="0" y1="0" x2="1" y2="1">
          <stop offset="0" stop-color="var(--blue-dark)"/>
          <stop offset="0.5" stop-color="var(--blue-light)"/>
          <stop offset="1" stop-color="#2a7cbf"/>
        </linearGradient>
      </defs>
      <polygon points="0,0 178,0 157,18 138,104 114,111 17,194 0,230" fill="url(#blueFacetB)"/>
    </svg>
    <svg class="corner corner--right" viewBox="0 0 178 230" role="img" aria-label="Rote polygonale Eckdekoration">
      <defs>
        <linearGradient id="redFacetB" x1="1" y1="0" x2="0" y2="1">
          <stop offset="0" stop-color="var(--red-dark)"/>
          <stop offset="0.5" stop-color="var(--red-light)"/>
          <stop offset="1" stop-color="#c02e26"/>
        </linearGradient>
      </defs>
      <polygon points="178,0 0,0 21,18 40,104 64,111 161,194 178,230" fill="url(#redFacetB)"/>
    </svg>
    <div class="emblem" role="img" aria-label="Platz für das Bildzeichen von Orno"></div>
    <p class="brand-name">Orno</p>
    <div class="motto-band"><p class="motto" lang="ar">إنما المؤمنون أخوة</p></div>
  </section>

</div>
</body>
</html>
```